Hockey Habits Poster Board for a Girls Youth Hockey Team

I'd like to have a (2) sided poster board created for our hockey team. The poster board will be 2'x4'. There are (4) different types of team play as follows:

Offense w/Puck - You have the puck and your team is on offense
-------------
Offense wo/Puck - You do not have the puck but your teammate does
-------------
Defense on/Puck - Your opponent has the puck and you are the closest defender from your team to the opponent with the puck
-------------
Defense away/Puck - Your opponent has the puck and you are not the closes defender from your team to the opponent with the puck
--------------
Individual habits are what we want every player to have regardless of the team situation. I think I'd like to have the individual habits on both sides of the poster board.

I'm open to ideas but I thought it would be cool to have a hockey rink in the background. This is also for a girls hockey team so if you are going to use a hockey player - please make sure the player is female.

Target Market(s)

Youth Hockey

Industry/Entity Type

Youth Sports - Hockey

Font styles to use
Serif
Sans Serif

Colors
0054AA
0677BA
7BADD7
CADEEF
E8F1F8
00AB8E
00BBA5
67D7C9
C6EFE9
E9F9F6

Requirements
Must have
• All of the individual habits on both sides. All the defensive habits on one side and the offensive habits on the other side.
Nice to have
• I'd like to see an image of a hockey rink on both sides of the poster as well as a female hockey player
Should not have
• boys

```html
<!DOCTYPE html>
<html lang="en">
<head>
<meta charset="utf-8">
<title>Hockey Habits</title>
<link href="https://fonts.googleapis.com/css2?family=Audiowide&family=Roboto+Condensed:wght@400;700&display=swap" rel="stylesheet">
<style>
  :root{
    --backdrop:#e4e4e6;
    --ink:#222;
    --panel:#eff0f4;
    --red:#e05a57;
    --red-soft:#f29b9a;
    --gold:#d8b04a;
    --gold-soft:#f4d77c;
    --green:#6cbf4a;
    --green-soft:#a9e48c;
    --purple:#c25ee0;
    --blue:#4a86df;
    --night:#06123d;
    --arena:#1c54ac;
    --ice:#cfe2f5;
  }
  *{box-sizing:border-box;margin:0;padding:0}
  html,body{width:848px;height:1200px;overflow:hidden;background:var(--backdrop)}
  body{font-family:"Roboto Condensed",Arial,sans-serif;color:var(--ink)}
  .poster{position:absolute;left:124px;top:0;width:600px;height:1200px;background:#fff;overflow:hidden}

  /* hero */
  .hero{position:absolute;left:0;top:0;width:600px;height:300px;
    background:
      radial-gradient(ellipse 60px 40px at 50px 90px,rgba(255,255,255,.75),transparent 70%),
      radial-gradient(ellipse 60px 40px at 550px 80px,rgba(255,255,255,.75),transparent 70%),
      radial-gradient(ellipse 260px 70px at 300px 230px,rgba(190,220,250,.6),transparent 70%),
      linear-gradient(180deg,var(--night) 0%,#0b2a77 30%,var(--arena) 55%,#6f9fd8 80%,var(--ice) 100%);}
  .hero-player{position:absolute;left:440px;top:85px;width:100px;height:205px;border-radius:40px 40px 6px 6px;
    background:linear-gradient(180deg,#1a2240,#0e1530)}
  .hero-ice{position:absolute;left:0;top:250px;width:600px;height:70px}
  .title{position:absolute;left:0;width:600px;text-align:center;font-family:"Audiowide",sans-serif;
    color:#fff;line-height:1;letter-spacing:1px;transform-origin:50% 0;transform:scaleY(1.2)}
  .title-top{top:86px;left:-8px;font-size:70px;text-shadow:2px 2px 0 #c0122f,-2px -2px 0 #c0122f,2px -2px 0 #c0122f,-2px 2px 0 #c0122f,0 3px 0 #6a1a5a}
  .title-bottom{top:168px;left:-18px;font-size:70px;text-shadow:2px 2px 0 #f28a12,-2px -2px 0 #f28a12,2px -2px 0 #f28a12,-2px 2px 0 #f28a12,0 3px 0 #c25a10}

  /* section pills */
  .pill{position:absolute;height:22px;border-radius:11px;color:#fff;display:flex;align-items:center;justify-content:center;gap:8px;
    box-shadow:0 5px 5px -3px rgba(0,0,0,.3)}
  .pill-label{font-family:"Audiowide",sans-serif;font-size:15px;letter-spacing:.5px}
  .pill-note{font-size:14px}
  .pill-individual{left:202px;top:288px;width:202px;background:var(--red)}
  .pill-offense-puck{left:89px;top:586px;width:455px;background:var(--purple)}
  .pill-offense-away{left:58px;top:894px;width:495px;background:var(--blue)}

  /* skill rows */
  .skills{position:absolute;left:14px;width:572px;display:flex;justify-content:space-between;align-items:flex-end}
  .skill{display:flex;flex-direction:column;align-items:center;gap:5px;font-weight:700;font-size:10px;white-space:nowrap}
  .skill svg{width:26px;height:26px}
  .sep{width:1px;height:7px;margin-bottom:2px}
  .skills-individual{top:322px;left:18px;width:570px}
  .skills-individual .sep{background:var(--red)}
  .skills-individual svg{fill:var(--red)}
  .skills-offense-puck{top:624px;left:14px;width:552px}
  .skills-offense-puck .sep{background:var(--purple)}
  .skills-offense-puck svg{fill:var(--purple)}
  .skills-offense-away{top:936px;left:15px;width:572px}
  .skills-offense-away .skill{font-size:9px}
  .skills-offense-away .sep{background:var(--blue)}
  .skills-offense-away svg{fill:var(--blue)}

  /* tier boards */
  .board{position:absolute;left:17px;width:568px;height:190px;display:flex;box-shadow:0 2px 4px rgba(0,0,0,.12)}
  .board-individual{top:376px}
  .board-offense-puck{top:681px;height:184px}
  .board-offense-away{top:995px;height:185px}
  .tier{position:relative;padding-top:34px}
  .tier-average{width:167px;background:var(--panel)}
  .tier-good{width:211px;background:#fff}
  .tier-great{width:190px;background:var(--panel)}
  .tier-head{position:absolute;top:8px;left:0;height:19px;font-family:"Audiowide",sans-serif;font-size:13px;
    display:flex;align-items:center;padding-left:16px;color:#3a2a2a}
  .tier-average .tier-head{width:132px;background:var(--red-soft);border-left:10px solid var(--red)}
  .tier-good .tier-head{left:24px;width:150px;background:var(--gold-soft);border-left:14px solid var(--gold);padding-left:12px}
  .tier-great .tier-head{left:15px;width:172px;background:var(--green-soft);border-left:12px solid var(--green);padding-left:6px}
  .habits{list-style:none;font-size:7.8px;line-height:9.6px}
  .tier-average .habits{padding:0 8px 0 19px}
  .tier-good .habits{padding:0 40px 0 43px}
  .tier-great .habits{padding:0 8px 0 31px}
  .habits li{position:relative;margin-bottom:9.6px}
  .habits li::before{content:"";position:absolute;left:-12px;top:1px;width:7px;height:7px;border-radius:50%;
    border:1px solid #666;background:radial-gradient(circle,#555 0 1.6px,transparent 2px)}
  .habits li.plain::before{display:none}
</style>
</head>
<body>
<main class="poster">

  <header class="hero" role="img" aria-label="Floodlit indoor hockey arena with a female player in a number 5 jersey seen from behind">
    <div class="hero-player"></div>
    <svg class="hero-ice" viewBox="0 0 600 70" preserveAspectRatio="none" aria-hidden="true">
      <path d="M0 25 Q300 -5 600 25 L600 70 L0 70 Z" fill="#fff"/>
      <path d="M0 25 Q300 -5 600 25" stroke="#7aa6d6" stroke-width="2" fill="none"/>
    </svg>
  </header>
  <h1 class="title title-top">HOCKEY</h1>
  <p class="title title-bottom">HABITS</p>

  <!-- individual -->
  <div class="pill pill-individual"><span class="pill-label">INDIVIDUAL</span></div>
  <nav class="skills skills-individual">
    <div class="skill"><svg viewBox="0 0 24 24"><path d="M3 15l6-6 3 3-6 6zM12 12l6-6 3 3-6 6z"/></svg>COMPETE</div><span class="sep"></span>
    <div class="skill"><svg viewBox="0 0 24 24"><path d="M12 2a8 8 0 0 0-8 8c0 3 2 5 3 6v6h8v-3h3v-4h2l-2-4A8 8 0 0 0 12 2z"/></svg>MENTALTOUGHNESS</div><span class="sep"></span>
    <div class="skill"><svg viewBox="0 0 24 24"><path d="M12 1c1 5 7 7 7 14a7 7 0 0 1-14 0c0-4 3-5 3-9 2 2 2 3 2 4 2-2 2-5 2-9z"/></svg>SPIRIT</div><span class="sep"></span>
    <div class="skill"><svg viewBox="0 0 24 24"><path d="M2 22h20v-4h-5v-4h-5v-4H7v4H2z"/><circle cx="17" cy="6" r="4"/></svg>EFFORT</div><span class="sep"></span>
    <div class="skill"><svg viewBox="0 0 24 24"><circle cx="5" cy="6" r="2"/><circle cx="12" cy="5" r="2"/><circle cx="19" cy="6" r="2"/><path d="M3 9h4v12H3zM10 8h4v13h-4zM17 9h4v12h-4z"/></svg>TEAMWORK</div><span class="sep"></span>
    <div class="skill"><svg viewBox="0 0 24 24"><path d="M12 3a7 7 0 0 0-4 13v3h8v-3a7 7 0 0 0-4-13zM9 20h6v2H9z"/></svg>HOCKEY IQ</div>
  </nav>
  <section class="board board-individual">
    <div class="tier tier-average"><h2 class="tier-head">AVERAGE</h2>
      <ul class="habits">
        <li>Watches during games &amp; doesn't work hard in practice</li>
        <li>Gets easily upset with everyone</li>
        <li>ALL-IN when team is winning</li>
        <li>Works hard when they want to</li>
        <li>They should get me the puck</li>
        <li>Thinks they know hockey</li>
      </ul></div>
    <div class="tier tier-good"><h2 class="tier-head">GOOD</h2>
      <ul class="habits">
        <li>Competes during games</li>
        <li>Park Mistakes (their's, teammates, referees)</li>
        <li>ALL-IN during all games</li>
        <li>Works as hard as their opponents</li>
        <li class="plain">I'll pass if I have to</li>
        <li>Knows that they need to learn</li>
      </ul></div>
    <div class="tier tier-great"><h2 class="tier-head">GREAT</h2>
      <ul class="habits">
        <li>Competes during games and practices</li>
        <li>Able to turn negative situations into positive energy and use it!</li>
        <li>ALL-IN during practice and games</li>
        <li>Their effort matches the best of their ability - they give 100% all the time!</li>
        <li>Enjoys setting up their teammates for an easy goal as much as scoring!</li>
        <li>Watches pro league, college, youth games trying to always learn</li>
      </ul></div>
  </section>

  <!-- offense with puck -->
  <div class="pill pill-offense-puck"><span class="pill-label">OFFENSE W/PUCK</span><span class="pill-note">You have the puck and your team is on offense</span></div>
  <nav class="skills skills-offense-puck">
    <div class="skill"><svg viewBox="0 0 24 24"><circle cx="16" cy="3" r="2.5"/><path d="M14 6l-5 3-3 5 2 1 3-4 2 1-3 6H4v2h9l2-5 3 3v5h2v-6l-3-4 2-4 3 2 1-2z"/></svg>SKATING WITH THE PUCK</div><span class="sep"></span>
    <div class="skill"><svg viewBox="0 0 24 24"><path d="M4 3l12 12h5v3h-7L2 5zM20 3L8 15H3v3h7L22 5z"/><rect x="9" y="20" width="6" height="3" rx="1"/></svg>STICKHANDLING</div><span class="sep"></span>
    <div class="skill"><svg viewBox="0 0 24 24"><path d="M3 21v-6a8 8 0 0 1 8-8h5V3l7 7-7 7v-4h-5a4 4 0 0 0-4 4v4z"/></svg>MAKING A PASS</div><span class="sep"></span>
    <div class="skill"><svg viewBox="0 0 24 24"><path d="M2 8l10 10h6v3h-7L0 10z"/><circle cx="19" cy="13" r="2.5"/><path d="M19 4l3 3-3 3z"/></svg>SHOOTING</div><span class="sep"></span>
    <div class="skill"><svg viewBox="0 0 24 24"><path d="M11 2h2v8h-2zM12 0l4 4h-8zM3 6l5 5-1 1-5-5zM21 6l-5 5 1 1 5-5z"/><circle cx="12" cy="18" r="4"/></svg>PLAY &nbsp;MAKING</div>
  </nav>
  <section class="board board-offense-puck">
    <div class="tier tier-average"><h2 class="tier-head">AVERAGE</h2>
      <ul class="habits">
        <li>Eyes always on the puck</li>
        <li>Control puck in front of body</li>
        <li>Blindly hitting the puck</li>
        <li>Shoots towards the net wherever they are</li>
        <li>Making a deke, pass or shot once D is on you</li>
      </ul></div>
    <div class="tier tier-good"><h2 class="tier-head">GOOD</h2>
      <ul class="habits">
        <li>Eyes on puck see game in peripheral vision</li>
        <li>Control puck side to side</li>
        <li>Making a pass toward teammate</li>
        <li>Shoots hard towards the net</li>
        <li>Making a deke, pass or shot before the D is on you</li>
      </ul></div>
    <div class="tier tier-great"><h2 class="tier-head">GREAT</h2>
      <ul class="habits">
        <li>Eyes on the game peripheral vision for puck</li>
        <li>Control puck in all positions</li>
        <li>Make a pass with eyes up tape to tape to where the player is going</li>
        <li>Finds a good shooting lane and shoots as hard as they possibly can</li>
        <li>Anticipate the play and play in areas D can't get you</li>
      </ul></div>
  </section>

  <!-- offense without puck -->
  <div class="pill pill-offense-away"><span class="pill-label">OFFENSE WO/PUCK</span><span class="pill-note">You do not have the puck but your teammate does</span></div>
  <nav class="skills skills-offense-away">
    <div class="skill"><svg viewBox="0 0 24 24"><path d="M1 7l10 10h6v3h-7L-1 9z"/><circle cx="21" cy="17" r="2.5"/></svg>RECEIVING A PASS</div><span class="sep"></span>
    <div class="skill"><svg viewBox="0 0 24 24"><path d="M2 3h20v14H2zm2 2v10h16V5z"/><path d="M5 6l5 5M19 6l-5 5M5 14l4-4M19 14l-4-4"/><circle cx="19" cy="19" r="4"/></svg>REBOUNDS, TIPS, SCREENS</div><span class="sep"></span>
    <div class="skill"><svg viewBox="0 0 24 24"><path d="M10 2a8 8 0 1 0 4.9 14.3l6 6 1.5-1.5-6-6A8 8 0 0 0 10 2zm0 2a6 6 0 1 1 0 12 6 6 0 0 1 0-12z"/><path d="M7 10l2 2 4-4 1 1-5 5-3-3z"/></svg>FINDING OPEN ICE</div><span class="sep"></span>
    <div class="skill"><svg viewBox="0 0 24 24"><circle cx="12" cy="4" r="3"/><path d="M9 8h6v9H9zM5 19h14v3H5z"/></svg>POSITIONING (TRADITIONAL ROLES)</div><span class="sep"></span>
    <div class="skill"><svg viewBox="0 0 24 24"><path d="M2 7h12V3l7 6-7 6v-4H2zM22 15H12v-2l-7 5 7 5v-3h10z"/></svg>READY TO SWITCH TO DEFENSE</div>
  </nav>
  <section class="board board-offense-away">
    <div class="tier tier-average"><h2 class="tier-head">AVERAGE</h2>
      <ul class="habits">
        <li>Eyes always on the puck</li>
        <li>Control puck in front of body</li>
        <li>Blindly hitting the puck</li>
        <li>Shoots towards the net wherever they are</li>
        <li>Making a deke, pass or shot once D is on you</li>
      </ul></div>
    <div class="tier tier-good"><h2 class="tier-head">GOOD</h2>
      <ul class="habits">
        <li>Eyes on puck see game in peripheral vision</li>
        <li>Control puck side to side</li>
        <li>Making a pass toward teammate</li>
        <li>Shoots hard towards the net</li>
        <li>Making a deke, pass or shot before the D is on you</li>
      </ul></div>
    <div class="tier tier-great"><h2 class="tier-head">GREAT</h2>
      <ul class="habits">
        <li>Eyes on the game peripheral vision for puck</li>
        <li>Control puck in all positions</li>
        <li>Make a pass with eyes up tape to tape to where the player is going</li>
        <li>Finds a good shooting lane and shoots as hard as they possibly can</li>
        <li>Anticipate the play and play in areas D can't get you</li>
      </ul></div>
  </section>

</main>
</body>
</html>
```